A standard Business and Stock Market Website

We are looking for a well designed and attractive website design which deals on the day to day business activities and stock market performance across the globe.

A good reference website for my proposed website is http://quillharbor.com and http://vkp.com

We are basically featuring the leading stock markets such as Pell marsh stock market and others. The Business name is Quarry lane.
I require very bright colors such as blue, green, black, golden.

Easy nagivating of the website is require and the design should also be responsive on mobile devices.

Designs for three pages. The first design should be for the home page, the second for the Economy/ stockmarkets, Third, business and tech. The home image would also feature stocks, economy, business, tech.

```html
<!DOCTYPE html>
<html lang="en">
<head>
<meta charset="utf-8">
<title>Quarry Lane — Markets, Business and Tech</title>
<link href="https://fonts.googleapis.com/css2?family=Montserrat:wght@400;600;700&family=Open+Sans:wght@400;600;700&display=swap" rel="stylesheet">
<style>
:root{
  --blue:#1aa9e0;
  --blue-dark:#0f7fb0;
  --ink:#222;
  --muted:#666;
  --page:#ececec;
  --card:#fff;
  --line:#dedede;
  --nav:#1c1c1c;
  --search-band:#3d3d3d;
  --footer:#4b4e52;
  --footer-base:#2a2b2d;
  --red:#d9232a;
  --green:#2a9a3c;
  --ad:#55585c;
}
*{box-sizing:border-box;margin:0;padding:0}
html,body{width:1200px;height:2913px;overflow:hidden}
body{background:var(--page);font-family:"Open Sans",Arial,sans-serif;color:var(--ink);position:relative}
a{color:inherit;text-decoration:none}
.abs{position:absolute}

/* header */
.site-header{left:0;top:0;width:1200px;height:101px;background:#fff;border-top:4px solid var(--blue)}
.brand{left:97px;top:18px;font-family:"Montserrat",sans-serif;font-weight:700;color:var(--blue);line-height:1}
.brand .top{font-size:42px;letter-spacing:3px;display:block}
.brand .bottom{font-size:20px;letter-spacing:13px;display:block;margin-top:3px;color:#333}
.date-block{left:826px;top:28px;display:flex;align-items:center;gap:14px}
.date-block .date{font-family:"Montserrat",sans-serif;font-weight:700;font-size:17px;line-height:1.35;color:#222}
.search-icon{left:1046px;top:30px}

.main-nav{left:0;top:101px;width:1200px;height:39px;background:var(--nav);display:flex}
.main-nav a{font-family:"Montserrat",sans-serif;font-weight:700;font-size:16px;letter-spacing:1px;color:#fff;display:flex;align-items:center;justify-content:center;height:39px}
.main-nav a+a{border-left:2px solid #555}

.hero{left:0;top:140px;width:1200px;height:462px;background:linear-gradient(120deg,#0d1a2b 0%,#2b4766 45%,#5f7f9f 70%,#1a2a3d 100%)}

.search-band{left:0;top:602px;width:1200px;height:91px;background:var(--search-band)}
.search-band .field{position:absolute;left:318px;top:23px;width:404px;height:43px;background:#fff;font-size:17px;color:#777;padding:10px 18px}
.search-band .go{position:absolute;left:722px;top:23px;width:117px;height:43px;background:var(--blue);color:#fff;font-family:"Montserrat",sans-serif;font-weight:700;font-size:17px;display:flex;align-items:center;justify-content:center;clip-path:polygon(0 0,100% 0,92% 100%,0 100%)}

/* market data */
.market-card{left:97px;top:728px;width:990px;height:247px;background:var(--card)}
.market-card h2{position:absolute;left:16px;top:14px;font-family:"Montserrat",sans-serif;font-size:21px;font-weight:700}
.quote-table{position:absolute;left:16px;top:49px;width:347px;border-collapse:collapse;font-size:10px;line-height:1.2}
.quote-table th{text-align:left;background:#e6eef8;color:#1b3f78;font-weight:700;padding:1px 4px;border:1px solid #bfcfe3;height:17px}
.quote-table td{padding:1px 4px;font-weight:600;border-bottom:1px solid #eee;height:19px}
.quote-table tr.first td{background:#dcdcdc}
.quote-table .dn{color:var(--red)}
.quote-table .up{color:var(--green)}
.table-note{position:absolute;left:16px;top:212px;font-size:9.5px;color:#888;line-height:1.35;width:347px}
.table-note .link{color:var(--blue-dark)}
.table-note .more{position:absolute;right:0;top:0;color:var(--blue-dark);font-weight:700}
.index-chart{position:absolute;left:369px;top:49px;width:350px}
.index-chart .head{display:flex;justify-content:space-between;font-size:10.5px;font-weight:700;color:#1b5f96}

.today{position:absolute;left:738px;top:10px;width:245px}
.today h3{font-family:"Montserrat",sans-serif;font-weight:700;font-size:16px;margin-bottom:10px}
.holiday{width:235px;height:144px;background:linear-gradient(135deg,#0c0c0c 0%,#0c0c0c 70%,var(--blue) 70%);border-left:6px solid var(--blue);padding:10px 12px;color:#fff;position:relative}
.holiday .title{background:var(--blue);font-family:"Montserrat",sans-serif;font-weight:700;font-size:22px;display:inline-block;padding:2px 8px;margin:-4px 0 10px -6px}
.holiday p{font-size:11px;font-weight:700;line-height:1.35;width:160px}
.holiday p span{color:var(--blue)}
.holiday .tag{position:absolute;right:10px;bottom:12px;font-family:"Montserrat",sans-serif;font-size:10px;font-weight:700;text-align:right;line-height:1.2}
.today .pager{display:flex;justify-content:space-between;align-items:center;margin-top:8px;width:235px;font-size:10.5px;font-weight:700;color:var(--blue-dark)}

/* resource tabs */
.resource-tabs{left:97px;top:1006px;width:990px;height:56px;background:var(--card);display:flex;align-items:center;padding-left:16px}
.resource-tabs a{font-family:"Montserrat",sans-serif;font-weight:700;font-size:15.5px;letter-spacing:.5px;color:var(--blue);margin-right:22px}
.resource-tabs a.current{color:#111}

/* video */
.news-feature{left:97px;top:1084px;width:682px;height:398px;background:linear-gradient(135deg,#7a7f86 0%,#b7b9bc 40%,#6c6a68 75%,#3a3b3d 100%)}
.news-feature h2{position:absolute;left:0;right:0;top:124px;text-align:center;color:#fff;font-family:"Montserrat",sans-serif;font-weight:700;font-size:33px;letter-spacing:4px}
.news-feature .watch{position:absolute;left:206px;top:250px;width:270px;height:46px;background:var(--blue);color:#fff;font-family:"Montserrat",sans-serif;font-weight:700;font-size:16px;display:flex;align-items:center;justify-content:center;gap:12px}

/* articles */
.related-head{left:97px;top:1511px;width:682px;height:54px;background:var(--card);font-family:"Montserrat",sans-serif;font-weight:700;font-size:20px;letter-spacing:1px;color:#444;padding:15px 16px}
.article-list{left:97px;top:1592px;width:682px;height:768px;background:var(--card)}
.article{position:absolute;left:16px;width:650px;height:126px}
.article .thumb{position:absolute;left:0;top:0;width:188px;height:126px}
.article .meta{position:absolute;left:204px;top:14px;width:450px}
.article .kicker{font-family:"Montserrat",sans-serif;font-size:13.5px;color:#777;letter-spacing:.5px}
.article h3{font-family:"Montserrat",sans-serif;font-weight:700;font-size:15.5px;color:var(--blue);margin:3px 0 6px;white-space:nowrap}
.article p{font-size:13.5px;font-weight:600;color:#555;line-height:1.45}

/* sidebar */
.sidebar{left:802px;top:1084px;width:285px;height:1276px;background:var(--card)}
.sidebar .label{position:absolute;left:20px;font-family:"Montserrat",sans-serif;font-weight:700;font-size:15px}
.sidebar .news-date{position:absolute;left:20px;top:56px;font-size:10.5px;color:#888;font-weight:700}
.sidebar .news-text{position:absolute;left:20px;top:76px;width:245px;font-family:"Montserrat",sans-serif;font-size:14.5px;color:var(--blue);line-height:1.45}
.tweet{position:absolute;left:20px;width:245px;border-top:1px solid var(--line);padding-top:8px;font-size:11px;line-height:1.45;color:#333}
.tweet .who{font-family:"Montserrat",sans-serif;font-weight:700;font-size:15px;color:var(--blue);letter-spacing:1px}
.tweet .dot{position:absolute;right:4px;top:10px;width:12px;height:12px;border-radius:50%;background:var(--blue)}
.tweet .link{color:var(--blue-dark)}
.tweet .actions{display:flex;gap:16px;margin-top:8px;align-items:center}
.tweet .actions span{width:10px;height:10px;background:var(--blue-dark);border-radius:50%}
.tweet .media{margin:8px 0 0 0;height:126px}
.ad-slot{position:absolute;left:21px;top:928px;width:245px;height:324px;background:var(--ad);color:var(--blue);font-family:"Montserrat",sans-serif;font-weight:700;text-align:center;padding-top:108px}
.ad-slot .t1{font-size:19px}
.ad-slot .t2{font-size:19px;margin-top:24px;color:#fff}

/* subscribe */
.subscribe{left:0;top:2412px;width:1200px;height:132px;background:#e9e9e9;border-top:4px solid #333}
.subscribe .pitch{position:absolute;left:97px;top:42px;font-family:"Montserrat",sans-serif;font-weight:600;font-size:15.5px;line-height:1.6;color:#333;letter-spacing:.3px}
.subscribe .email{position:absolute;left:447px;top:44px;width:307px;height:44px;border:1px solid #999;background:#fff;font-size:11px;color:#777;padding:14px 20px;letter-spacing:.5px}
.subscribe .social{position:absolute;left:796px;top:44px;display:flex;border:1px solid #999}
.subscribe .social span{width:49.5px;height:42px;display:flex;align-items:center;justify-content:center}
.subscribe .social span+span{border-left:1px solid #999}
.subscribe .social i{width:11px;height:11px;border-radius:50%;background:#555;display:block}

/* footer */
.site-footer{left:0;top:2544px;width:1200px;height:317px;background:var(--footer);color:#fff}
.footer-col{position:absolute;top:48px}
.footer-col h4{font-family:"Montserrat",sans-serif;font-weight:700;font-size:16px;letter-spacing:1px;margin-bottom:8px}
.footer-col li{list-style:none;font-family:"Montserrat",sans-serif;font-weight:600;font-size:13px;line-height:23px}
.footer-col .icons{display:flex;gap:13px;margin-top:18px}
.footer-col .icons i{width:18px;height:18px;background:#fff;display:block;border-radius:3px}
.base-bar{left:0;top:2861px;width:1200px;height:52px;background:var(--footer-base);color:#fff;font-family:"Montserrat",sans-serif;font-weight:700;font-size:14px}
.base-bar .copy{position:absolute;left:97px;top:17px}
.base-bar .policy{position:absolute;right:113px;top:17px}
</style>
</head>
<body>

<header class="site-header abs">
  <a class="brand abs" href="#"><span class="top">QUARRY</span><span class="bottom">LANE</span></a>
  <div class="date-block abs">
    <svg width="38" height="40" viewBox="0 0 38 40" aria-hidden="true">
      <rect x="2" y="5" width="34" height="33" rx="3" fill="none" stroke="#1aa9e0" stroke-width="3"/>
      <rect x="2" y="5" width="34" height="9" fill="#1aa9e0"/>
      <rect x="9" y="1" width="4" height="8" fill="#1aa9e0"/><rect x="25" y="1" width="4" height="8" fill="#1aa9e0"/>
      <g fill="#1aa9e0"><rect x="8" y="18" width="5" height="4"/><rect x="16" y="18" width="5" height="4"/><rect x="24" y="18" width="5" height="4"/><rect x="8" y="25" width="5" height="4"/><rect x="16" y="25" width="5" height="4"/><rect x="24" y="25" width="5" height="4"/><rect x="8" y="31" width="5" height="4"/><rect x="16" y="31" width="5" height="4"/></g>
    </svg>
    <div class="date">Monday, 26th<br>September, 2016</div>
  </div>
  <svg class="search-icon abs" width="36" height="36" viewBox="0 0 36 36" aria-label="Search">
    <circle cx="14" cy="14" r="11" fill="none" stroke="#1aa9e0" stroke-width="3.5"/>
    <line x1="22" y1="22" x2="33" y2="33" stroke="#1aa9e0" stroke-width="4.5" stroke-linecap="round"/>
  </svg>
</header>

<nav class="main-nav abs">
  <a href="#" style="width:375px">HOME</a>
  <a href="#" style="width:427px">ECONOMY / STOCKMARKETS</a>
  <a href="#" style="width:398px">BUSINESS AND TECH</a>
</nav>

<div class="hero abs" role="img" aria-label="Businessman in a suit touching a glowing rising bar and line chart on a transparent screen"></div>

<div class="search-band abs">
  <div class="field">Enter symbol, name or keyword</div>
  <a class="go" href="#">Search</a>
</div>

<section class="market-card abs">
  <h2>MARKET DATA</h2>
  <table class="quote-table">
    <tr><th>Index</th><th>Value</th><th>Change Net / %</th></tr>
    <tr class="first"><td>Quarry Lane</td><td>5383.12</td><td class="dn">-48.97 ▼ 0.90%</td></tr>
    <tr><td>Quarry Lane -100 (QLX)</td><td>4863.62</td><td class="dn">-54.66 ▼ 1.11%</td></tr>
    <tr><td>Pre-Market (QLX)</td><td>4926.43</td><td class="up">8.15 ▲ 0.17%</td></tr>
    <tr><td>After Hours (QLX)</td><td>4861.27</td><td class="dn">-2.35 ▼ 0.05%</td></tr>
    <tr><td>HIA</td><td>19762.60</td><td class="dn">-57.18 ▼ 0.29%</td></tr>
    <tr><td>Broad 500</td><td>2238.83</td><td class="dn">-10.43 ▼ 0.46%</td></tr>
    <tr><td>Ramsay 2000</td><td>1357.13</td><td class="dn">-6.05 ▼ 0.44%</td></tr>
  </table>
  <div class="table-note">Data as of Dec 30, 2016<br><span class="link">Try for Free: Tallow LiveQuotes Platform</span><span class="more">➔ View Major Indices</span></div>

  <div class="index-chart">
    <div class="head"><span>Tallow Composite</span><span>Volume: 1,564,773,601</span></div>
    <svg width="350" height="170" viewBox="0 0 350 170" aria-label="Intraday index chart">
      <g font-size="9" fill="#555" font-family="Open Sans, sans-serif">
        <text x="4" y="36">5425</text><text x="4" y="94">5400</text><text x="4" y="152">5375</text>
        <text x="50" y="166">10:00 AM</text><text x="138" y="166">12:00 PM</text><text x="222" y="166">2:00 PM</text><text x="300" y="166">4:00 PM</text>
      </g>
      <line x1="36" y1="8" x2="36" y2="155" stroke="#999"/>
      <line x1="36" y1="155" x2="340" y2="155" stroke="#999"/>
      <line x1="36" y1="22" x2="340" y2="22" stroke="#333" stroke-width="1.5"/>
      <path d="M40 42 L48 60 L55 52 L62 75 L70 68 L78 90 L85 84 L92 104 L100 96 L108 112 L116 106 L124 118 L134 110 L144 124 L154 118 L164 128 L176 122 L188 132 L200 126 L212 134 L224 128 L236 136 L250 130 L264 138 L278 132 L292 140 L306 134 L318 142 L328 128 L336 118 L336 155 L40 155 Z" fill="#6fc7db" stroke="#1b8fb3" stroke-width="1.2"/>
    </svg>
  </div>

  <div class="today">
    <h3>TODAY AT QUARRY LANE</h3>
    <div class="holiday">
      <div class="title">Market Holiday</div>
      <p>QUARRY LANE U.S. equity, options and futures markets will be closed on <span>January 2, 2017.</span></p>
      <div class="tag">QUARRY<br>LANE</div>
    </div>
    <div class="pager">
      <svg width="10" height="14" viewBox="0 0 10 14"><path d="M9 0 L0 7 L9 14 Z" fill="#1aa9e0"/></svg>
      <span>Holiday Schedule</span>
      <svg width="10" height="14" viewBox="0 0 10 14"><path d="M1 0 L10 7 L1 14 Z" fill="#1aa9e0"/></svg>
    </div>
  </div>
</section>

<nav class="resource-tabs abs">
  <a class="current" href="#">RESOURCES</a>
  <a href="#">TRADER UPDATES</a>
  <a href="#">MARKET STATUS</a>
  <a href="#">HOURS</a>
  <a href="#">SUBSCRIPTIONS</a>
  <a href="#">CONNECT</a>
</nav>

<section class="news-feature abs" role="img" aria-label="Business team discussing documents around a meeting table">
  <h2>QUARRY LANE NEWS</h2>
  <a class="watch" href="#">Watch Today News
    <svg width="12" height="16" viewBox="0 0 12 16"><path d="M2 1 L10 8 L2 15" fill="none" stroke="#fff" stroke-width="3"/></svg>
  </a>
</section>

<div class="related-head abs">RELATED ARTICLES</div>

<section class="article-list abs">
  <article class="article" style="top:12px">
    <div class="thumb" role="img" aria-label="Printed table of interest rates" style="background:linear-gradient(135deg,#e7dcc6,#a79a83)"></div>
    <div class="meta"><div class="kicker">INSIGHTS</div><h3>How Interest Rates Affect The Stock Market</h3><p>Whether you're buying lunch, a home or a stock, you're influenced by interest rates.</p></div>
  </article>
  <article class="article" style="top:162px">
    <div class="thumb" role="img" aria-label="Illustrated house with the year 2008 and a price tag" style="background:linear-gradient(135deg,#efeadb,#c9c2a8)"></div>
    <div class="meta"><div class="kicker">INVESTING</div><h3>Wealth Effect</h3><p>The wealth effect is a psychological phenomenon that causes people to spend more as the value of their assets rises. The premise is that when consumers' homes or investment portfolios increase ...</p></div>
  </article>
  <article class="article" style="top:311px">
    <div class="thumb" role="img" aria-label="Columned stock exchange building facade" style="background:linear-gradient(135deg,#4a5058,#9aa1a8)"></div>
    <div class="meta"><div class="kicker">FINANCIAL ADVISOR</div><h3>Advising FAs: How To Explaining Stocks to a Client</h3><p>Without a doubt, common stocks are one of the greatest tools ever invented for building wealth.</p></div>
  </article>
  <article class="article" style="top:461px">
    <div class="thumb" role="img" aria-label="Glowing stock ticker board with numbers" style="background:linear-gradient(135deg,#0b1a4a,#3b2a7a 60%,#b0202a)"></div>
    <div class="meta"><div class="kicker">INSIGHTS</div><h3>A Breakdown on How the Stock Market Works</h3><p>Learn what it means to own stocks and shares, why shares exist, and how you buy and sell them.</p></div>
  </article>
  <article class="article" style="top:610px">
    <div class="thumb" role="img" aria-label="Illustrated stock certificate, shop and office tower" style="background:linear-gradient(135deg,#f4f4f0,#b7ae95)"></div>
    <div class="meta"><div class="kicker">INVESTING</div><h3>How The Stock Market Works</h3><p>When you buy a stock, you buy a piece of a company.</p></div>
  </article>
</section>

<aside class="sidebar abs">
  <div class="label" style="top:22px">NEWS</div>
  <div class="news-date">DECEMBER 19, 2016</div>
  <div class="news-text">QUARRY LANE LOREM IPSUM DOLAR SMIT AT SMET THAT LOREM IPSUM DOLAR SMIT AT SMET THAT...</div>
  <div class="label" style="top:192px">FOLLOW <span style="font-weight:600">@ QUARRY LANE</span></div>

  <div class="tweet" style="top:220px">
    <i class="dot"></i>
    <div class="who">QUARRY LANE</div>
    <div>Even the bull is in the holiday spirit @ Harbor City Exchange</div>
    <div class="link">snapgrid.com/p/BOqtbywAneF/</div>
    <div class="actions"><span></span><span></span></div>
  </div>

  <div class="tweet" style="top:356px">
    <i class="dot"></i>
    <div style="font-weight:700;font-size:12px">Quarry Lane Released</div>
    <div style="font-weight:700">Linden Works, Inc.</div>
    <div style="color:#888">@LindenWorks</div>
    <div>Tune in: January 4th, as our President, Rob Tanner joins <span class="link">@Corvix</span> to ring the bell at the View Here: <span class="link">qlane.link/bell4</span></div>
    <div class="media" role="img" aria-label="Ring bell event graphic" style="background:linear-gradient(135deg,#e2e2e6,#c4c4cc)"></div>
    <div class="actions"><span></span><span></span></div>
  </div>

  <div class="tweet" style="top:673px">
    <i class="dot"></i>
    <div class="who">QUARRY LANE</div>
    <div>Today the cast of the <span class="link">@MarlowStage</span> tapped their way to the floor</div>
    <div class="media" role="img" aria-label="Performers on the trading floor" style="height:112px;background:linear-gradient(135deg,#1b2233,#4b5770 60%,#2a2f3a)"></div>
    <div class="actions"><span></span><span></span></div>
  </div>

  <div class="ad-slot"><div class="t1">YOUR ADD HERE</div><div class="t2">325 x 435</div></div>
</aside>

<section class="subscribe abs">
  <div class="pitch">SUBSCRIBE TO LATEST NEWS &amp; GREAT<br>DEALS WE OFFER</div>
  <div class="email">ENTER YOUR EMAIL ADDRESS ...
    <svg style="position:absolute;right:14px;top:14px" width="18" height="13" viewBox="0 0 18 13"><rect x="1" y="1" width="16" height="11" fill="none" stroke="#777" stroke-width="1.4"/><path d="M1 1 L9 7 L17 1" fill="none" stroke="#777" stroke-width="1.4"/></svg>
  </div>
  <div class="social"><span><i></i></span><span><i></i></span><span><i></i></span><span><i></i></span><span><i></i></span><span><i></i></span></div>
</section>

<footer class="site-footer abs">
  <div class="footer-col" style="left:101px">
    <h4>ABOUT EXCHANGE</h4>
    <ul><li>About Our Business</li><li>Investors</li><li>Media</li><li>Careers</li></ul>
  </div>
  <div class="footer-col" style="left:390px">
    <h4>TOOLS &amp; FEATURES</h4>
    <ul><li>Products</li><li>Trade</li><li>Clear</li><li>Data</li><li>Tech</li><li>Benchmarks</li><li>Reports</li><li>Contact</li></ul>
  </div>
  <div class="footer-col" style="left:676px">
    <h4>QUARRY LANE</h4>
    <ul><li>List</li><li>Trade</li><li>Data &amp; Tech</li><li>Governance Services</li><li>Insights</li><li>Regulation</li><li>HCX Connect</li><li>Subscriptions</li><li>Media Center</li><li>Contact</li></ul>
  </div>
  <div class="footer-col" style="left:967px">
    <h4>FOLLOW US</h4>
    <div class="icons"><i></i><i></i><i></i><i></i><i></i></div>
  </div>
</footer>

<div class="base-bar abs">
  <span class="copy">© Copyright 2016 Quarry Lane.All rights Reserved.</span>
  <span class="policy">PRIVACY &amp; POLICY</span>
</div>

</body>
</html>
```